Willowmere Equine Sanctuary Flyer Urgent

Willowmere Equine Sanctuary

Rescue • Rehabilitation • Sanctuary

Willowmere Equine Sanctuary provides a safe and ethical refuge for horses, ponies and donkeys who have nowhere else to go. Some arrive needing rehabilitation and careful retraining, while others find permanent sanctuary here due to age, injury or behavioural needs.

Our mission is simple: to improve the physical and psychological wellbeing of every animal in our care.

At Willowmere we focus on:
• Rescue and rehabilitation of horses in need
• Lifetime sanctuary for those who cannot be rehomed
• Education and advocacy for responsible horse care
• Equine rehabilitation services to help horses recover and thrive

Sponsor a Horse

One of the most meaningful ways to support our work is by sponsoring one of our residents. Each horse, pony or donkey only has one sponsor!

Your sponsorship helps provide:
• Hay and feed
• Veterinary care
• Hoof trimming and routine health care
• Rugs, shelter and daily care

Many of our horses will live out their lives here, and sponsorship ensures they are safe, well fed and cared for every single day.

Sponsorship starts from $15 - $25 per week / $60 -$100 per month.

How You Can Help

• Sponsor a horse
• Make a donation
• Share our work with others

Your support helps us continue to say yes to horses who need a second chance.

📍 Willowmere Park, Victoria
📧 carla@willowmerepaddock.org

📞 0400 519 627

Font styles to use
Serif
Sans Serif

Colors
F0912C
F2A743
F7CA91
FBE8D2
FDF5EE
EE7325
F08F49
F5BC92
FAE3D3
FDF4ED

Requirements
Should not have
• Photos not provided by Willowmere

```html
<!DOCTYPE html>
<html lang="en">
<head>
<meta charset="utf-8">
<title>Willowmere Equine Sanctuary – Sponsor a Horse</title>
<link href="https://fonts.googleapis.com/css2?family=Poppins:wght@400;500;600;700;800&family=Bebas+Neue&display=swap" rel="stylesheet">
<style>
  :root{
    --red:#e84f37;
    --orange:#f58a33;
    --amber:#f0912c;
    --gold:#f2a743;
    --peach:#f7ca91;
    --cream:#fde8d2;
    --brown:#4a2413;
    --ink:#1b1b1b;
    --paper:#ffffff;
  }
  *{box-sizing:border-box;margin:0;padding:0}
  html,body{width:960px;height:1200px;overflow:hidden;background:#fff}
  body{font-family:"Poppins",sans-serif;color:var(--ink)}
  .flyer{position:relative;width:960px;height:1200px;background:var(--paper);overflow:hidden}
  .abs{position:absolute}

  /* brand */
  .brand{left:68px;top:96px;display:flex;align-items:center;gap:12px}
  .brand-name{font-size:19px;font-weight:600;color:var(--red);line-height:1.15;width:168px}
  .brand-square{width:58px;height:58px;background:var(--orange)}

  /* headline */
  .headline{left:68px;top:176px;line-height:52px}
  .headline .strong{display:block;font-size:62px;font-weight:800;color:var(--red);letter-spacing:-1px}
  .headline .soft{display:block;font-size:60px;font-weight:500;color:var(--ink);letter-spacing:-0.5px}

  /* pillars */
  .pillars{left:68px;top:404px;display:flex}
  .pillar{display:flex;flex-direction:column;align-items:center;padding:0 8px}
  .pillar:first-child{padding-left:2px}
  .pillar + .pillar{border-left:1px solid #cfcfcf}
  .pillar-icon{width:36px;height:36px;border-radius:50%;background:var(--orange);display:flex;align-items:center;justify-content:center;margin-bottom:4px}
  .pillar-label{font-size:19px;font-weight:700}

  /* hero photo placeholder */
  .hero{left:438px;top:40px;width:522px;height:430px;
    background:radial-gradient(ellipse at 40% 40%,var(--orange) 0%,var(--gold) 45%,var(--peach) 70%,rgba(255,255,255,0) 78%);}

  .intro{left:71px;top:488px;width:790px;font-size:13.4px;line-height:16px;color:#222}

  /* mission */
  .mission{left:71px;top:558px;display:flex;gap:16px;align-items:flex-start}
  .mission h2{font-size:19px;font-weight:800;line-height:22px}
  .mission p{font-size:13.2px;line-height:16px;color:#222}
  .accent{color:var(--amber)}

  .focus-title{left:71px;top:630px;font-size:19px;font-weight:800}
  .focus-list{left:75px;top:664px;list-style:none;width:360px}
  .focus-list li{font-size:15.5px;font-weight:600;line-height:15px;margin-bottom:20px;padding-left:17px;position:relative}

  .tick{position:relative}
  .tick::before{content:"";position:absolute;left:0;top:2px;width:11px;height:11px;border-radius:50%;background:var(--red)}
  .tick::after{content:"";position:absolute;left:3.5px;top:4px;width:3px;height:5px;border:solid #fff;border-width:0 1.6px 1.6px 0;transform:rotate(45deg)}
  .tick.dark::before{background:var(--brown)}

  .photo{top:866px;width:176px;height:158px;border-radius:16px}
  .photo-a{left:71px;background:linear-gradient(135deg,#6e5a3c,#b08a5a 55%,#8c8f5a)}
  .photo-b{left:264px;background:linear-gradient(135deg,#4d3e2e,#c7a27a 50%,#8d7a58)}

  .support{left:71px;top:1043px;width:380px;font-size:15px;font-weight:700;line-height:18px}
  .contact{left:71px;top:1090px;display:flex;gap:28px;font-size:13.5px;align-items:center}
  .contact span{display:flex;align-items:center;gap:6px}
  .links{left:72px;top:1114px;display:flex;height:24px;font-size:11.5px;font-weight:600;color:#fff}
  .links .email{background:var(--orange);width:177px;border-radius:6px 0 0 6px;display:flex;align-items:center;justify-content:center;font-size:10px}
  .links .web{background:var(--red);width:195px;border-radius:0 6px 6px 0;display:flex;align-items:center;justify-content:center}

  /* sponsor card */
  .tab{left:564px;top:562px;width:264px;height:44px;background:var(--brown);border-radius:16px 16px 0 0;color:#fff;font-size:19px;font-weight:800;display:flex;align-items:center;justify-content:center}
  .card{left:515px;top:605px;width:362px;height:252px;background:var(--orange);border-radius:16px;overflow:hidden}
  .card-lead{background:var(--red);height:101px;padding:12px 36px 12px 28px;color:var(--cream);font-size:14.2px;font-weight:600;line-height:16.5px}
  .card h3{font-size:17.5px;font-weight:800;color:var(--ink);margin:12px 0 6px 28px}
  .card ul{list-style:none;margin-left:30px}
  .card li{font-size:13px;font-weight:600;color:#fff;line-height:25px;padding-left:17px}
  .card li.tick::before{top:7px}
  .card li.tick::after{top:9px}

  .note{left:515px;top:870px;width:340px;font-size:13.2px;line-height:16px;color:#222}
  .banner{left:515px;top:934px;width:358px;height:31px;background:var(--red);border-radius:5px;color:#fff;font-family:"Bebas Neue",sans-serif;font-size:28px;display:flex;align-items:center;justify-content:center;letter-spacing:.5px}

  .price{top:979px;height:47px;border:1px solid #666;border-top-color:transparent}
  .price .amount{position:absolute;left:0;right:0;top:-12px;text-align:center;font-family:"Bebas Neue",sans-serif;font-size:44px;line-height:44px;background:#fff;margin:0 10px}
  .price .per{position:absolute;left:0;right:0;bottom:-12px;text-align:center;font-size:19px;line-height:20px}
  .price .per span{background:#fff;padding:0 2px}
  .price-week{left:515px;width:152px}
  .price-week .per{letter-spacing:2px}
  .price-month{left:712px;width:165px}
  .or{left:678px;top:1000px;width:28px;height:28px;border-radius:50%;background:var(--amber);color:#fff;font-family:"Bebas Neue",sans-serif;font-size:24px;display:flex;align-items:center;justify-content:center}

  .divider{left:515px;top:1053px;width:368px;height:1px;background:#d5d5d5}
  .help-title{left:517px;top:1064px;font-size:19px;font-weight:800}
  .help-row{position:absolute;left:513px;top:1098px;width:372px;display:flex;list-style:none}
  .help-row li{font-size:14px;font-weight:600;line-height:19px;padding-left:16px}
  .help-row li:nth-child(1){width:99px}
  .help-row li:nth-child(2){width:95px}
  .help-row li::before{top:4px}
  .help-row li::after{top:6px}
</style>
</head>
<body>
<main class="flyer">

  <div class="abs brand">
    <div class="brand-name">Willowmere Equine Sanctuary</div>
    <div class="brand-square"></div>
  </div>

  <h1 class="abs headline">
    <span class="strong">WILLOW</span>
    <span class="strong">MERE</span>
    <span class="soft">Equine</span>
    <span class="soft">Sanctuary</span>
  </h1>

  <div class="abs pillars">
    <div class="pillar">
      <div class="pillar-icon"><svg width="18" height="18" viewBox="0 0 18 18"><path d="M9 3v12M3 9h12" stroke="#fff" stroke-width="2.2" stroke-linecap="round"/></svg></div>
      <div class="pillar-label">Rescue</div>
    </div>
    <div class="pillar">
      <div class="pillar-icon"><svg width="18" height="18" viewBox="0 0 18 18"><path d="M9 15s-6-3.6-6-7.6A3 3 0 0 1 9 6a3 3 0 0 1 6 1.4C15 11.4 9 15 9 15z" fill="none" stroke="#fff" stroke-width="1.6"/></svg></div>
      <div class="pillar-label">Rehabilitation</div>
    </div>
    <div class="pillar">
      <div class="pillar-icon"><svg width="18" height="18" viewBox="0 0 18 18"><path d="M3 9l6-5 6 5v6H3z" fill="none" stroke="#fff" stroke-width="1.6" stroke-linejoin="round"/></svg></div>
      <div class="pillar-label">Sanctuary</div>
    </div>
  </div>

  <div class="abs hero" role="img" aria-label="Group of horses and ponies standing before an orange watercolour wash"></div>

  <p class="abs intro">Willowmere Equine Sanctuary provides a safe and ethical refuge for horses, ponies and donkeys who have nowhere else to go. Some arrive needing rehabilitation and careful retraining, while others find permanent sanctuary here due to age, injury or behavioural needs.</p>

  <section class="abs mission">
    <svg width="48" height="48" viewBox="0 0 48 48">
      <circle cx="22" cy="26" r="19" fill="none" stroke="#e84f37" stroke-width="5"/>
      <circle cx="22" cy="26" r="11" fill="none" stroke="#e84f37" stroke-width="4"/>
      <circle cx="22" cy="26" r="4" fill="#e84f37"/>
      <path d="M22 26L42 6" stroke="#e84f37" stroke-width="3" stroke-linecap="round"/>
      <path d="M38 3l7 0-3 7z" fill="#e84f37"/>
    </svg>
    <div>
      <h2>OUR <span class="accent">MISSION</span></h2>
      <p>To improve the physical and psychological<br>wellbeing of every animal in our care.</p>
    </div>
  </section>

  <h2 class="abs focus-title">AT WILLOWMERE <span class="accent">WE FOCUS ON</span></h2>
  <ul class="abs focus-list">
    <li class="tick">Rescue and rehabilitation of horses<br>in need</li>
    <li class="tick">Lifetime sanctuary for those who cannot<br>be rehomed</li>
    <li class="tick">Education and advocacy for responsible<br>horse care</li>
    <li class="tick">Equine rehabilitation services to help<br>horses recover and thrive</li>
  </ul>

  <div class="abs photo photo-a" role="img" aria-label="Photo of a young deer and a dog greeting each other"></div>
  <div class="abs photo photo-b" role="img" aria-label="Photo of small ponies standing together in a paddock"></div>

  <p class="abs support">Your support helps us continue to say yes to horses who need a second chance.</p>

  <div class="abs contact">
    <span><svg width="13" height="13" viewBox="0 0 16 16"><path d="M4 1l3 3-2 2a9 9 0 0 0 5 5l2-2 3 3-2 3C7 15 1 9 1 3z" fill="#e84f37"/></svg>0400 519 627</span>
    <span><svg width="11" height="14" viewBox="0 0 12 16"><path d="M6 0a6 6 0 0 1 6 6c0 4-6 10-6 10S0 10 0 6a6 6 0 0 1 6-6z" fill="#e84f37"/><circle cx="6" cy="6" r="2.2" fill="#fff"/></svg>Willowmere Park, Victoria</span>
  </div>
  <div class="abs links">
    <div class="email">carla@willowmerepaddock.org</div>
    <div class="web">www.willowmerepaddock.org</div>
  </div>

  <div class="abs tab">SPONSOR A HORSE</div>
  <section class="abs card">
    <p class="card-lead">One of the most meaningful ways to support our work is by sponsoring one of our residents. Each horse, pony or donkey only has one sponsor!</p>
    <h3>Your sponsorship helps provide</h3>
    <ul>
      <li class="tick dark">Hay and feed</li>
      <li class="tick dark">Veterinary care</li>
      <li class="tick dark">Hoof trimming and routine health care</li>
      <li class="tick dark">Rugs, shelter and daily care</li>
    </ul>
  </section>

  <p class="abs note">Many of our horses will live out their lives here, and sponsorship ensures they are safe, well fed and cared for every single day.</p>

  <div class="abs banner">SPONSORSHIP STARTS FROM</div>
  <div class="abs price price-week">
    <div class="amount">$15-$25</div>
    <div class="per"><span>per week</span></div>
  </div>
  <div class="abs or">/</div>
  <div class="abs price price-month">
    <div class="amount">$60-$100</div>
    <div class="per"><span>per month</span></div>
  </div>

  <div class="abs divider"></div>
  <h2 class="abs help-title">HOW YOU <span class="accent">CAN HELP</span></h2>
  <ul class="help-row">
    <li class="tick">Sponsor a<br>horse</li>
    <li class="tick">Make a<br>donation</li>
    <li class="tick">Share our work<br>with others</li>
  </ul>

</main>
</body>
</html>
```